Banner to celebrate Pellway Journeys 40 years in business. Will be used on our social media channels.

Hello
We would like a banner created to celebrate 40 years in business with tagline "service through experience since 1983"
also add our website pellwayjourneys.com.au
Banner size must be : 650 x 150px
open to suggestions

Target Market(s)

current and prospective clients

Industry/Entity Type

Travel & Tourism (Business Travel)

Colors
0054AA
0677BA
7BADD7
CADEEF
E8F1F8

Requirements
Must have
• use current theme of our website www.pellwayjourneys.com.au. Keep simple and effective.
Nice to have
• use one image that I have provided
Should not have
• multiple graphics

```html
<!DOCTYPE html>
<html lang="en">
<head>
<meta charset="UTF-8">
<title>Pellway Journeys – 40 Years Banner</title>
<link rel="stylesheet" href="https://fonts.googleapis.com/css2?family=Roboto:wght@400;500;700;900&display=swap">
<style>
  :root {
    --navy-deep: #1c3766;
    --navy: #24427a;
    --brand-blue: #0054AA;
    --mid-blue: #0677BA;
    --sky: #7BADD7;
    --mist: #CADEEF;
    --ice: #E8F1F8;
    --white: #ffffff;
    --accent: #e9a23b;
    --logo-navy: #1f3a6e;
  }
  * { margin: 0; padding: 0; box-sizing: border-box; }
  html, body {
    width: 1200px;
    height: 277px;
    overflow: hidden;
    background: var(--white);
    font-family: "Roboto", Arial, sans-serif;
  }
  .banner {
    position: relative;
    width: 1200px;
    height: 277px;
    display: flex;
    overflow: hidden;
  }
  .hero {
    position: relative;
    width: 852px;
    height: 100%;
  }
  .hero-photo {
    position: absolute;
    inset: 0;
    background:
      linear-gradient(90deg, var(--navy-deep) 0%, var(--navy) 38%, rgba(36,66,122,0.55) 58%, rgba(36,66,122,0) 78%),
      linear-gradient(90deg, #6f86a6 0%, #a9b8c9 45%, #7d8a99 70%, #c4ccd6 100%);
  }
  .tagline {
    position: absolute;
    left: 52px;
    top: 56px;
    color: var(--white);
    font-weight: 700;
    font-size: 41px;
    line-height: 61px;
    letter-spacing: -0.2px;
  }
  .brand-panel {
    flex: 1;
    display: flex;
    flex-direction: column;
    align-items: center;
    justify-content: center;
    gap: 30px;
    background: var(--white);
  }
  .brand-name {
    color: var(--logo-navy);
    font-weight: 900;
    font-size: 40px;
    letter-spacing: -0.5px;
    white-space: nowrap;
  }
  .site-button {
    display: flex;
    align-items: center;
    justify-content: center;
    width: 280px;
    height: 44px;
    background: var(--accent);
    color: var(--white);
    font-weight: 500;
    font-size: 23px;
    text-decoration: none;
  }
</style>
</head>
<body>
  <div class="banner">
    <section class="hero">
      <div class="hero-photo" role="img" aria-label="Photo of a business traveller with a handbag checking her phone in an airport terminal, tinted with a deep blue overlay on the left"></div>
      <h1 class="tagline">Service<br>through Experience<br>Since 1983</h1>
    </section>
    <aside class="brand-panel">
      <div class="brand-name">Pellway Journeys</div>
      <a class="site-button" href="#">pellwayjourneys.com.au</a>
    </aside>
  </div>
</body>
</html>
```